Business Cards - Brightway Harbor

need to design unique business card for my mortgage business. I need to design credit card style business card for my business or any unique idea that you might have

Target Market(s)

Home Loan customers

Industry/Entity Type

Mortgage Brokerage

Contact Information for Business Card

please design credit card style or very unique style business card

Colors

Designer to choose colors to be used in the design.

Requirements
Must have
• Name
• position
• Phone number
• fax number
• email address
• website address
• social media address
• All above fields will be provided once design in finalised

```html
<!DOCTYPE html>
<html lang="en">
<head>
<meta charset="utf-8">
<title>Brightway Harbor – Business Cards</title>
<link href="https://fonts.googleapis.com/css2?family=Cinzel:wght@400;700&family=Open+Sans:wght@400;600&display=swap" rel="stylesheet">
<style>
  :root {
    --bg: #3a3230;
    --card: #0c0c0d;
    --orange: #f08a1c;
    --blue: #0a33d6;
    --teal: #1aa6c8;
    --white: #f2f2f2;
    --silver: #c9c9cc;
  }
  * { margin: 0; padding: 0; box-sizing: border-box; }
  html, body { width: 1200px; height: 900px; overflow: hidden; }
  body {
    background: var(--bg);
    display: flex;
    align-items: center;
    justify-content: center;
    gap: 50px;
    font-family: "Open Sans", sans-serif;
  }
  .card {
    position: relative;
    width: 540px;
    height: 310px;
    background: var(--card);
    border-radius: 4px;
    overflow: hidden;
    box-shadow: 0 14px 30px rgba(0,0,0,.45);
  }
  /* front */
  .brand {
    position: absolute;
    left: 30px;
    top: 104px;
    width: 252px;
  }
  .brand-mark {
    display: flex;
    align-items: center;
    gap: 8px;
  }
  .brand-dot {
    width: 12px; height: 12px;
    background: var(--teal);
    border-radius: 50%;
    flex: none;
  }
  .brand-name {
    font-family: "Cinzel", serif;
    font-weight: 700;
    font-size: 19px;
    line-height: 1.1;
    white-space: nowrap;
    color: var(--blue);
  }
  .divider {
    position: absolute;
    left: 292px;
    top: 60px;
    width: 1px;
    height: 108px;
    background: var(--teal);
  }
  .contact {
    position: absolute;
    left: 312px;
    top: 58px;
  }
  .person-name {
    font-family: "Cinzel", serif;
    font-weight: 700;
    font-size: 16px;
    color: var(--orange);
    letter-spacing: .5px;
  }
  .person-role {
    font-size: 12px;
    color: var(--white);
    margin-bottom: 10px;
  }
  .contact-list { list-style: none; }
  .contact-list li {
    display: flex;
    align-items: center;
    gap: 8px;
    font-size: 12px;
    line-height: 19px;
    color: var(--white);
  }
  .contact-list svg { width: 10px; height: 10px; fill: var(--orange); flex: none; }
  .band {
    position: absolute;
    left: 0; right: 0;
    top: 212px;
    height: 58px;
    background: var(--blue);
    display: flex;
    align-items: center;
    padding-left: 232px;
    gap: 6px;
  }
  .social {
    width: 22px; height: 22px;
    background: var(--white);
  }
  /* back */
  .back {
    display: flex;
    align-items: center;
    justify-content: center;
  }
  .back .brand-name { color: var(--silver); font-size: 32px; }
</style>
</head>
<body>
  <section class="card front">
    <div class="brand">
      <div class="brand-mark">
        <span class="brand-dot"></span>
        <span class="brand-name">Brightway Harbor</span>
      </div>
    </div>
    <div class="divider"></div>
    <div class="contact">
      <div class="person-name">DANIEL REYES</div>
      <div class="person-role">Managing Director</div>
      <ul class="contact-list">
        <li><svg viewBox="0 0 10 10"><path d="M2 0h2l1 2.5-1.3 1A5 5 0 0 0 6.5 6.3L7.5 5 10 6v2a2 2 0 0 1-2 2A8 8 0 0 1 0 2a2 2 0 0 1 2-2z"/></svg>(044) 555 0142</li>
        <li><svg viewBox="0 0 10 10"><path d="M2 0h5v3H2zM0 3h10v7H0zm2 2v1h2V5zm4 0v1h2V5zM2 7v1h2V7zm4 0v1h2V7z"/></svg>(044) 555 0143</li>
        <li><svg viewBox="0 0 10 10"><path d="M0 1h10v1.5L5 6 0 2.5zm0 3 5 3.5L10 4v5H0z"/></svg>info@brightwayharbor.com</li>
        <li><svg viewBox="0 0 10 10"><circle cx="5" cy="5" r="5"/></svg>www.brightwayharbor.com</li>
      </ul>
    </div>
    <div class="band">
      <span class="social"></span>
      <span class="social"></span>
      <span class="social"></span>
    </div>
  </section>

  <section class="card back">
    <span class="brand-name">Brightway Harbor</span>
  </section>
</body>
</html>
```